Business Card Design Project

We need a Business Card for an Mechanical Engineering firm in Singapore. The design should be Modern & Technical looking, yet eye catching.

Our company deals in Cutting Tools & Machine Accessories for the Manufacturing Industries such as Oil & Gas, Aero Space, etc... For more information on our Company, you can either email me or view our website www.valtrion.com.sg.

We are trying to revamp our image to give our consumers a fresh new perspective to our company, so we welcome all ideas.

Industry/Entity Type

Business

Requirements
Must have
• Must incorporate New Company Logo into the card as shown in Uploaded file.

```html
<!DOCTYPE html>
<html lang="en">
<head>
<meta charset="utf-8">
<title>Valtrion Tools – Business Card</title>
<link rel="stylesheet" href="https://fonts.googleapis.com/css2?family=Roboto:wght@300;400&display=swap">
<style>
  :root {
    --page-bg: #ffffff;
    --card-bg: #f6f6f8;
    --brand-red: #8b1020;
    --brand-red-deep: #6e0a14;
    --band-grey: #8a8a8d;
    --text-grey: #7b7b7e;
    --white: #ffffff;
  }
  * { margin: 0; padding: 0; box-sizing: border-box; }
  html, body {
    width: 1200px; height: 928px; overflow: hidden;
    background: var(--page-bg);
    font-family: "Roboto", Arial, sans-serif;
    font-weight: 300;
  }
  .canvas { position: relative; width: 1200px; height: 928px; }

  .card { position: absolute; width: 550px; height: 292px; }

  /* Front card sits on top of the back card */
  .card-front { left: 91px; top: 189px; background: var(--card-bg); z-index: 2; }
  .brand {
    position: absolute; right: 46px; top: 52px;
    display: flex; align-items: center; gap: 8px;
    color: var(--brand-red); font-size: 22px; font-weight: 300;
    letter-spacing: 1px; text-transform: uppercase;
  }
  .brand-dot {
    width: 14px; height: 14px; border-radius: 50%;
    background: var(--brand-red);
  }
  .name-band {
    position: absolute; left: 0; right: 0; top: 125px; height: 39px;
    background: var(--band-grey);
    display: flex; align-items: center; padding-left: 51px;
  }
  .person-name { color: var(--white); font-size: 19px; font-weight: 300; }
  .person-role { color: var(--brand-red); font-size: 14px; margin-left: 34px; margin-top: 3px; }

  .contact-list {
    position: absolute; left: 48px; top: 190px;
    list-style: none; color: var(--text-grey); font-size: 13.5px; line-height: 18.3px;
  }
  .contact-list li { display: flex; align-items: center; }
  .contact-label {
    width: 16px; color: var(--brand-red); font-size: 7.5px; font-weight: 400;
  }
  .address {
    position: absolute; right: 46px; top: 190px;
    text-align: right; font-style: normal; text-transform: uppercase;
    color: var(--text-grey); font-size: 13.5px; line-height: 18.3px;
  }

  /* Back card */
  .card-back { left: 554px; top: 405px; background: var(--brand-red); z-index: 1; }
  .back-art {
    position: absolute; inset: 0;
    background: linear-gradient(135deg, var(--brand-red) 0%, var(--brand-red-deep) 100%);
  }
  .website {
    position: absolute; right: 29px; top: 242px;
    color: var(--white); font-size: 15px; font-weight: 400;
  }
</style>
</head>
<body>
<main class="canvas">
  <section class="card card-front">
    <div class="brand"><span class="brand-dot"></span><span>Valtrion Tools</span></div>
    <div class="name-band">
      <span class="person-name">Daniel K. Morrow</span>
      <span class="person-role">technical support</span>
    </div>
    <ul class="contact-list">
      <li><span class="contact-label">T</span>818.555.0142</li>
      <li><span class="contact-label">F</span>818.555.0143</li>
      <li><span class="contact-label">M</span>818.555.0178</li>
      <li><span class="contact-label">E</span>dmorrow@valtriontools.com</li>
    </ul>
    <address class="address">
      2450 Harbor View Ave.<br>
      Suite 300<br>
      Lakemont&nbsp; CA<br>
      90415
    </address>
  </section>

  <section class="card card-back">
    <div class="back-art" role="img" aria-label="Large overlapping brand symbol decoration in deep red tones"></div>
    <span class="website">valtriontools.com</span>
  </section>
</main>
</body>
</html>
```